Postcard Mail Out - Wendell

We are a real estate company. We need a post card to mail out to potential clients to try and sale their land. We will attached a couple of post cards that we like but we do not want to copy them completely. We do need to put the Fair Dwelling Access and the Homebroker logos with a disclosure saying not intended to solicit currently listed properties. The image below is what we had started working on. We would like to include something about farm land, timber, maybe a pond, something along those lines. The PDF Files attached are a flyer that was mailed out by another company that we do not want to copy completely. Attached also will be our company's Logo.

Requirements
Must have
• We do need to put the Fair Dwelling Access and the Homebroker logos with a disclosure saying not intended to solicit currently listed properties.<br/><br/>At Cal Moreno Summit Realty, we are blessed to have one of the very best Rural Land Specialists available. Wendell has years of experience promoting and selling rural land properties. Wendell has earned the trust of many landowners, as he is so PASSIONATE in all regards to rural land, farms and ranches. He has made a wide range of landowners very happy throughout his years in Real Estate. Call him today and show him your property, and he will provide you with a free analysis and strategy to maximize the return on your property.
Nice to have
• A picture of Wendell has been added to use on the back of the post card with his phone and number. It would be nice to have a east Texas scenery picture behind him instead of an office.<br/><br/>Please include front and back of post card in your submission.
Should not have
• Should not have Ferris Dunmore's information on the postcard. That post card was just to show what we was wanting. The agent we want listed is Wendell Pruitt and his phone number is (555)413-2086.

```html
<!DOCTYPE html>
<html lang="en">
<head>
<meta charset="utf-8">
<title>Wendell Pruitt – Rural Land Postcard</title>
<link rel="stylesheet" href="https://fonts.googleapis.com/css2?family=Days+One&family=Didact+Gothic&family=Fira+Sans:wght@700&family=Roboto+Condensed:wght@400;700&display=swap">
<style>
  :root {
    --page: #ffffff;
    --navy: #1f3a8c;
    --navy-deep: #142a6b;
    --gold: #c9a227;
    --ink: #1e1e2a;
    --heading-ink: #2a2f6b;
    --bullet: #3f6fd1;
    --veil: rgba(255,255,255,0.8);
    --white: #ffffff;
    --outline: #111111;
    --strip: rgba(20,42,107,0.82);
  }
  * { box-sizing: border-box; margin: 0; padding: 0; }
  html, body {
    width: 1200px; height: 483px; overflow: hidden;
    background: var(--page);
    font-family: "Didact Gothic", "Gill Sans", sans-serif;
    color: var(--ink);
  }
  .canvas { position: relative; width: 1200px; height: 483px; }

  /* ---------- Back of card ---------- */
  .card-back {
    position: absolute; left: 26px; top: 25px; width: 567px; height: 433px;
    overflow: hidden;
  }
  .scene-back {
    position: absolute; inset: 0;
    background:
      radial-gradient(ellipse 60% 45% at 52% 40%, #b7c9cf 0%, #7e8f78 45%, transparent 75%),
      linear-gradient(180deg, #4a3424 0%, #6b4a32 35%, #3f5a46 62%, #2f5b5a 80%, #244a4d 100%);
  }
  .info-panel { position: absolute; left: 58px; top: 48px; width: 451px; height: 335px; }
  .info-panel svg { position: absolute; inset: 0; }

  .title-pill {
    position: absolute; left: 81px; top: 26px; width: 286px; height: 31px;
    border-radius: 15px; background: var(--gold);
    font-family: "Fira Sans", sans-serif; font-weight: 700; font-size: 22px;
    color: var(--navy-deep); text-align: center; line-height: 31px;
  }
  .promise-list {
    position: absolute; left: 113px; top: 64px; list-style: none;
    font-size: 11px; line-height: 15.5px;
  }
  .promise-list li::before {
    content: ""; display: inline-block; width: 5px; height: 5px; border-radius: 50%;
    background: var(--bullet); margin-right: 7px; vertical-align: 2px;
  }
  .tools-heading {
    position: absolute; left: 38px; top: 131px;
    font-family: "Fira Sans", sans-serif; font-weight: 700; font-size: 11px;
    color: var(--heading-ink);
  }
  .tools-list {
    position: absolute; left: 38px; top: 146px; width: 390px; list-style: none;
    display: grid; grid-template-columns: 200px 190px; row-gap: 1px;
    font-size: 10.5px; line-height: 14px;
  }
  .tools-list span { display: inline-block; width: 24px; }
  .bio {
    position: absolute; left: 20px; top: 180px; width: 408px;
    font-size: 10.8px; line-height: 13.8px; text-align: justify;
  }
  .bio strong { font-family: "Fira Sans", sans-serif; color: var(--heading-ink); font-weight: 700; }

  .compliance {
    position: absolute; left: 58px; top: 392px; width: 451px; height: 32px;
    background: var(--strip); border-radius: 4px;
    display: flex; align-items: center; gap: 12px; padding: 0 10px;
    color: var(--white);
  }
  .mark {
    display: flex; align-items: center; gap: 5px; white-space: nowrap;
    font-family: "Fira Sans", sans-serif; font-weight: 700; font-size: 9.5px;
  }
  .mark-square { width: 12px; height: 12px; background: var(--white); }
  .disclosure { font-size: 8.5px; line-height: 10.5px; }

  /* ---------- Front of card ---------- */
  .card-front {
    position: absolute; left: 606px; top: 25px; width: 567px; height: 286px;
    overflow: hidden;
  }
  .scene-front {
    position: absolute; inset: 0;
    background:
      linear-gradient(180deg, rgba(120,170,220,0) 0%, rgba(120,170,220,0) 55%, #5f8a78 72%, #3f6f66 100%),
      linear-gradient(90deg, #4d4a3a 0%, #6f7a5a 30%, #5e8c4a 55%, #8fb8e0 78%, #cfe2f2 100%);
  }
  .agent-photo {
    position: absolute; left: 338px; top: 12px; width: 196px; height: 274px;
    border-radius: 60px 60px 0 0;
    background: linear-gradient(180deg, #c9a99a 0%, #1d2438 28%, #111725 100%);
    opacity: 0.9;
  }
  .brand {
    position: absolute; left: 110px; top: 112px; display: flex; align-items: center; gap: 6px;
    font-family: "Fira Sans", sans-serif; font-weight: 700; font-size: 13px; color: var(--white);
  }
  .brand-dot { width: 14px; height: 14px; border-radius: 50%; background: var(--white); }
  .agent-name {
    position: absolute; left: 20px; top: 146px; width: 420px; text-align: center;
    font-family: "Days One", sans-serif; font-size: 40px; line-height: 48px; color: var(--white);
    -webkit-text-stroke: 1.5px var(--outline); paint-order: stroke fill;
    text-shadow: 2px 2px 0 var(--outline);
  }
  .agent-phone {
    position: absolute; left: 20px; top: 194px; width: 420px; text-align: center;
    font-family: "Days One", sans-serif; font-size: 30px; line-height: 36px; color: var(--white);
    -webkit-text-stroke: 1.2px var(--outline); paint-order: stroke fill;
    text-shadow: 2px 2px 0 var(--outline);
  }
  .office-phone {
    position: absolute; left: 20px; top: 240px; width: 420px; text-align: center;
    font-family: "Roboto Condensed", sans-serif; font-weight: 700; font-size: 23px; line-height: 25px;
    color: var(--white); text-shadow: 1px 1px 2px rgba(0,0,0,0.6);
  }
  .website {
    position: absolute; left: 20px; top: 266px; width: 420px; text-align: center;
    font-family: "Roboto Condensed", sans-serif; font-weight: 400; font-size: 13px; line-height: 15px;
    color: var(--white); text-shadow: 1px 1px 2px rgba(0,0,0,0.6);
  }
</style>
</head>
<body>
<main class="canvas">

  <section class="card-back">
    <div class="scene-back" role="img" aria-label="Photo of a rocky grotto with a waterfall pouring into a clear green pool"></div>
    <div class="info-panel">
      <svg width="451" height="335" viewBox="0 0 451 335" aria-hidden="true">
        <rect x="0" y="0" width="451" height="335" fill="var(--veil)"/>
        <path d="M0 0 H451 V30 C300 8 130 20 0 58 Z" fill="var(--navy)"/>
        <path d="M0 58 C130 20 300 8 451 30" fill="none" stroke="var(--gold)" stroke-width="4"/>
        <path d="M0 322 C160 330 330 322 451 308 V335 H0 Z" fill="var(--navy)"/>
        <path d="M0 322 C160 330 330 322 451 308" fill="none" stroke="var(--gold)" stroke-width="4"/>
      </svg>
      <div class="title-pill">Fair Dwelling Access</div>
      <ul class="promise-list">
        <li>We Are Passionate about Rural Land</li>
        <li>We Identify Best Marketable Value of your Land</li>
        <li>We Target Likely Buyers Nationwide</li>
        <li>We Are Known for Honesty &amp; Integrity</li>
      </ul>
      <h3 class="tools-heading">Marketing Tools:</h3>
      <ol class="tools-list">
        <li><span>1.</span>Internet Marketing</li>
        <li><span>2.</span>Advertising on #1 Land Website</li>
        <li><span>3.</span>Email Newsletters</li>
        <li><span>4.</span>Social Media advertising</li>
      </ol>
      <p class="bio">At Cal Moreno Summit Realty, we are blessed to have one of the very best Rural Land Specialists available. <strong>Wendell</strong> has years of experience promoting and selling rural land properties. Wendell has earned the trust of many landowners, as he is so PASSIONATE in all regards to rural land, farms and ranches. He has made a wide range of landowners very happy throughout his years in Real Estate. Call him today and show him your property, and he will provide you with a free analysis and strategy to maximize the return on your property.</p>
    </div>
    <div class="compliance">
      <span class="mark"><span class="mark-square"></span>Fair Dwelling Access</span>
      <span class="mark"><span class="mark-square"></span>Homebroker</span>
      <p class="disclosure">This mailing is not intended to solicit currently listed properties.</p>
    </div>
  </section>

  <section class="card-front">
    <div class="scene-front" role="img" aria-label="Photo of a waterfall over limestone cliffs, green trees and a calm river under a blue sky"></div>
    <div class="agent-photo" role="img" aria-label="Photo of the agent smiling while talking on a phone, wearing a dark shirt"></div>
    <div class="brand"><span class="brand-dot"></span>Cal Moreno Summit Realty</div>
    <h1 class="agent-name">Wendell Pruitt</h1>
    <p class="agent-phone">(555)413-2086</p>
    <p class="office-phone">555-740-3198</p>
    <p class="website">summitlandco.com</p>
  </section>

</main>
</body>
</html>
```